International Trading Company, 'KIRO' needs a Business Card

The company name is "KIRO" and it has own logo design.
I'd like to use its logo on this business card.
I need two side Business Card.
I'll look forward to your great design.
Thank you very much in advance.

Contact Information for Business Card

Company Name : Kiro Harbour Limited
Information Example
Dorian Pallister
Mobile(use icon please) : 1 (212) 555-0143
Tel(use icon please) : 1 (212) 555-0178
Email(use icon please) : dorian27@kiroharbour-mail.com
Address(use icon please) : 482 Halden Ave, New York, NY 10160, USA

```html
<!DOCTYPE html>
<html lang="en">
<head>
<meta charset="utf-8">
<title>Kiro Harbour Limited – Business Card</title>
<link href="https://fonts.googleapis.com/css2?family=Source+Sans+3:wght@400;600;700&display=swap" rel="stylesheet">
<style>
  :root {
    --page-bg: #e8e6e3;
    --card-dark: #2c2c2e;
    --card-dark-light: #3b3b3e;
    --brand-red: #a91d28;
    --brand-red-light: #bf3640;
    --band-dark: #2a2a2c;
    --text-grey: #6e6e70;
    --text-light: #e4e4e4;
    --label-grey: #6c6c6e;
    --icon-grey: #8c8c8e;
  }
  * { box-sizing: border-box; margin: 0; padding: 0; }
  html, body {
    width: 1200px; height: 900px; overflow: hidden;
    background: var(--page-bg);
    font-family: "Source Sans 3", "Myriad Pro", Arial, sans-serif;
  }
  .sheet {
    width: 1200px; height: 900px;
    display: flex; flex-direction: column; align-items: center; justify-content: center;
    gap: 50px;
  }
  .card {
    position: relative;
    width: 630px; height: 360px;
    overflow: hidden;
    box-shadow: 0 10px 28px rgba(0,0,0,.22);
  }

  /* Contact side */
  .card--contact {
    background: linear-gradient(135deg, var(--card-dark) 0%, var(--card-dark-light) 100%);
  }
  .card--contact .bottom-band {
    position: absolute; left: 0; right: 0; bottom: 0; height: 20px;
    background: var(--brand-red);
  }
  .holder {
    position: absolute; top: 38px; right: 44px; text-align: right;
  }
  .holder__name {
    font-size: 34px; font-weight: 400; color: var(--text-grey); letter-spacing: .3px;
  }
  .holder__title {
    font-size: 12px; font-weight: 600; color: #b4b4b6; letter-spacing: 1px; margin-top: 4px;
  }
  .contact-label {
    position: absolute; top: 112px; left: 34px;
    width: 150px; height: 24px; padding-left: 10px;
    background: var(--label-grey);
    color: #f2f2f2; font-size: 15px; font-weight: 600; letter-spacing: 1px; line-height: 24px;
  }
  .contact-list {
    position: absolute; top: 150px; left: 34px; list-style: none;
  }
  .contact-list li {
    display: flex; align-items: center; gap: 14px;
    height: 36px; color: var(--text-light); font-size: 17px; letter-spacing: .3px;
  }
  .contact-list .icon { width: 22px; height: 22px; flex: none; }

  /* Logo side */
  .card--brand {
    background: linear-gradient(110deg, var(--brand-red) 0%, var(--brand-red) 55%, var(--brand-red-light) 100%);
  }
  .card--brand .bottom-band {
    position: absolute; left: 0; right: 0; bottom: 0; height: 58px;
    background: var(--band-dark);
  }
  .brand-name {
    position: absolute; left: 0; right: 0; top: 102px;
    text-align: center; color: var(--text-grey); font-weight: 700;
  }
  .brand-name__main {
    display: block; font-size: 100px; line-height: 1; letter-spacing: 4px;
  }
  .brand-name__sub {
    display: block; font-size: 24px; letter-spacing: 8px; margin-top: 4px;
  }
</style>
</head>
<body>
<main class="sheet">

  <section class="card card--contact" aria-label="Business card contact side">
    <div class="holder">
      <p class="holder__name">Dorian Pallister</p>
      <p class="holder__title">Managing Director</p>
    </div>
    <div class="contact-label">CONTACT</div>
    <ul class="contact-list">
      <li>
        <svg class="icon" viewBox="0 0 22 22" fill="none" stroke="var(--icon-grey)" stroke-width="1.4" aria-hidden="true">
          <path d="M4 11 L11 4.5 L18 11 M6 9.5 V17 H16 V9.5 M9.5 17 V13 H12.5 V17"/>
        </svg>
        <span>482 Halden Ave, New York, NY 10160, USA</span>
      </li>
      <li>
        <svg class="icon" viewBox="0 0 22 22" fill="none" stroke="var(--icon-grey)" stroke-width="1.4" aria-hidden="true">
          <rect x="3.5" y="6" width="15" height="10.5" rx="1"/>
          <path d="M3.5 6.5 L11 12 L18.5 6.5"/>
        </svg>
        <span>dorian27@kiroharbour-mail.com</span>
      </li>
      <li>
        <svg class="icon" viewBox="0 0 22 22" fill="none" stroke="var(--icon-grey)" stroke-width="1.4" aria-hidden="true">
          <path d="M6 4 L8.5 4 L10 8 L8.3 9.3 C9.2 11.4 10.6 12.8 12.7 13.7 L14 12 L18 13.5 L18 16 C18 17 17 18 16 18 C10 17.5 4.5 12 4 6 C4 5 5 4 6 4 Z"/>
        </svg>
        <span>1 (212) 555-0178</span>
      </li>
      <li>
        <svg class="icon" viewBox="0 0 22 22" fill="none" stroke="var(--icon-grey)" stroke-width="1.4" aria-hidden="true">
          <rect x="6.5" y="3" width="9" height="16" rx="1.5"/>
          <path d="M9.5 16 H12.5"/>
        </svg>
        <span>1 (212) 555-0143</span>
      </li>
    </ul>
    <div class="bottom-band"></div>
  </section>

  <section class="card card--brand" aria-label="Business card logo side">
    <h1 class="brand-name">
      <span class="brand-name__main">KIRO</span>
      <span class="brand-name__sub">HARBOUR LIMITED</span>
    </h1>
    <div class="bottom-band"></div>
  </section>

</main>
</body>
</html>
```